Business Card Design - Cryotherapy

We need a custom created business card for our company FrostLume Spa. We provide whole body cryotherapy and localized cryotherapy to our clients. Please be creative.
Please see our website for idea's on design.
www.frostlumespa.com
Industry/Entity Type
Business
Contact Information for Business Card
Name, Position, Phone Number, Address, Website, Email
Look and feel
Each slider illustrates characteristics of the customer's brand and the style your logo design should communicate.

```html
<!DOCTYPE html>
<html lang="en">
<head>
<meta charset="utf-8">
<title>FrostLume Spa — Business Card</title>
<link rel="stylesheet" href="https://fonts.googleapis.com/css2?family=Catamaran:wght@400;500;600&display=swap">
<style>
  :root {
    --stage: #e9eaec;
    --card: #ffffff;
    --navy: #14457a;
    --ink: #1b1b1b;
    --brand-green: #1f7f4a;
    --royal: #1552a8;
    --blue-deep: #0f4f8f;
    --blue-light: #1aa6c4;
    --teal: #1d9aa6;
    --green: #138a4c;
    --photo-warm-1: #f1d9c4;
    --photo-warm-2: #c99b7a;
    --photo-gray-1: #f4f4f4;
    --photo-gray-2: #b9b9b9;
  }
  * { box-sizing: border-box; margin: 0; padding: 0; }
  html, body {
    width: 1189px; height: 1200px; overflow: hidden;
    background: var(--stage);
    font-family: "Catamaran", "Segoe UI", sans-serif;
  }
  .card {
    position: absolute; left: 136px;
    width: 917px; height: 522px;
    background: var(--card);
    box-shadow: 0 6px 18px rgba(0,0,0,.18);
    overflow: hidden;
  }
  .card--front { top: 45px; }
  .card--back { top: 623px; }
  .card__art { position: absolute; inset: 0; width: 917px; height: 522px; }

  .holder { position: absolute; left: 38px; top: 36px; }
  .holder__name { font-size: 42px; font-weight: 500; color: var(--navy); line-height: 1; }
  .holder__role { font-size: 30px; font-weight: 400; color: var(--ink); line-height: 1; margin-top: 8px; }

  .brand-name {
    position: absolute; display: flex; align-items: center; gap: 14px;
    font-weight: 600; color: var(--brand-green); line-height: 1; white-space: nowrap;
  }
  .brand-name__dot { border-radius: 50%; background: var(--teal); flex: none; }
  .card--front .brand-name { left: 430px; top: 120px; font-size: 58px; }
  .card--front .brand-name__dot { width: 34px; height: 34px; }
  .card--back .brand-name { left: 0; right: 0; top: 222px; justify-content: center; font-size: 72px; }
  .card--back .brand-name__dot { width: 42px; height: 42px; }

  .contact {
    position: absolute; right: 44px; top: 386px;
    list-style: none; text-align: right;
  }
  .contact__item {
    display: flex; justify-content: flex-end; align-items: center; gap: 12px;
    font-size: 23px; color: var(--ink); line-height: 28.5px;
  }
  .contact__icon { width: 18px; height: 18px; flex: none; }

  .frame {
    position: absolute; left: 43px; top: 41px; width: 830px; height: 442px;
    border: 10px solid var(--royal);
  }
</style>
</head>
<body>

<section class="card card--front">
  <svg class="card__art" viewBox="0 0 917 522" aria-hidden="false">
    <defs>
      <linearGradient id="blueBand" x1="0" y1="0" x2="1" y2="1">
        <stop offset="0" stop-color="var(--blue-deep)"/>
        <stop offset="1" stop-color="var(--blue-light)"/>
      </linearGradient>
      <linearGradient id="swoosh" x1="0" y1="0" x2="1" y2="0">
        <stop offset="0" stop-color="var(--teal)"/>
        <stop offset="1" stop-color="var(--green)"/>
      </linearGradient>
      <linearGradient id="warmPhoto" x1="0" y1="0" x2="1" y2="1">
        <stop offset="0" stop-color="var(--photo-warm-1)"/>
        <stop offset="1" stop-color="var(--photo-warm-2)"/>
      </linearGradient>
      <linearGradient id="grayPhoto" x1="0" y1="0" x2="1" y2="0">
        <stop offset="0" stop-color="var(--card)"/>
        <stop offset=".5" stop-color="var(--photo-gray-1)"/>
        <stop offset="1" stop-color="var(--photo-gray-2)"/>
      </linearGradient>
    </defs>
    <path d="M0 140 Q 50 230 240 245 L 240 385 Q 110 388 0 400 Z" fill="url(#blueBand)" role="img" aria-label="Blue-toned photo of an athletic body for cryotherapy"/>
    <path d="M317 200 Q 660 150 917 410 L 917 418 Q 660 250 329 249 Z" fill="url(#swoosh)"/>
    <path d="M800 150 Q 880 110 917 130 L 917 400 Q 860 330 830 250 Q 805 200 800 150 Z" fill="url(#grayPhoto)" role="img" aria-label="Black and white beauty portrait photo"/>
    <circle cx="228" cy="265" r="102" fill="url(#warmPhoto)" stroke="var(--teal)" stroke-width="3" role="img" aria-label="Photo of a relaxing back massage"/>
  </svg>

  <div class="holder">
    <p class="holder__name">Daniel Ashford</p>
    <p class="holder__role">Manager</p>
  </div>

  <p class="brand-name"><span class="brand-name__dot"></span>FrostLume Spa</p>

  <ul class="contact">
    <li class="contact__item">(555) 214-7730
      <svg class="contact__icon" viewBox="0 0 18 18"><rect width="18" height="18" fill="var(--navy)"/><path d="M5 4c1 0 2 2 2 3s-1 1-1 2 2 3 3 3 1-1 2-1 3 1 3 2-1 2-2 2C7 15 3 11 3 6c0-1 1-2 2-2z" fill="#fff"/></svg>
    </li>
    <li class="contact__item">info@frostlumespa.com
      <svg class="contact__icon" viewBox="0 0 18 18"><rect width="18" height="18" fill="var(--navy)"/><rect x="3.5" y="5" width="11" height="8" fill="none" stroke="#fff" stroke-width="1.4"/><path d="M3.5 5l5.5 4.5L14.5 5" fill="none" stroke="#fff" stroke-width="1.4"/></svg>
    </li>
    <li class="contact__item">http://frostlumespa.com
      <svg class="contact__icon" viewBox="0 0 18 18"><rect width="18" height="18" fill="var(--navy)"/><circle cx="9" cy="9" r="5.5" fill="none" stroke="#fff" stroke-width="1.4"/><path d="M3.5 9h11M9 3.5c-2.5 3-2.5 8 0 11M9 3.5c2.5 3 2.5 8 0 11" fill="none" stroke="#fff" stroke-width="1.1"/></svg>
    </li>
    <li class="contact__item">2417 Lakeview Avenue Suite 210 Maple Grove,IL 60412
      <svg class="contact__icon" viewBox="0 0 18 18"><rect width="18" height="18" fill="var(--navy)"/><path d="M9 15s-4-4.5-4-7.5a4 4 0 0 1 8 0C13 10.5 9 15 9 15z" fill="#fff"/><circle cx="9" cy="7.5" r="1.5" fill="var(--navy)"/></svg>
    </li>
  </ul>
</section>

<section class="card card--back">
  <div class="frame"></div>
  <p class="brand-name"><span class="brand-name__dot"></span>FrostLume Spa</p>
</section>

</body>
</html>
```